Marwick Ostrand Law website for a law firm

modern clean website for a small boutique law firm. Based in Sacramento, CA and the Bay Area. Practice areas of Family Law, Civil litigation, and Criminal Defense. We already have a logo design as well as attorney pictures to include on page.
Would like images of California included on site.
Would like site to go with Logo that is already designed...blue/grey/white colors.

Industry/Entity Type

Law Firm

Number of Pages Required

5+ page

Requirements
Must have
• I already have several pages of content drafted. Just need the pages with images to input content. Must be clean and modern feel. Want it to reflect California and small boutique feel that is provided personalized legal attention.
• Must have a page where I can blog or post articles on.

```html
<!DOCTYPE html>
<html lang="en">
<head>
<meta charset="utf-8">
<title>Marwick & Ostrand Law</title>
<link rel="stylesheet" href="https://fonts.googleapis.com/css2?family=PT+Sans+Narrow&family=Lato:wght@400&display=swap">
<style>
  :root {
    --blue: #4a8acb;
    --panel-blue: #5b94cf;
    --ink: #222222;
    --text: #2b2b2b;
    --rust: #8f4a12;
    --grey: #8a8a8a;
    --white: #ffffff;
  }
  * { margin: 0; padding: 0; box-sizing: border-box; }
  html, body { width: 1200px; height: 1125px; overflow: hidden; background: var(--white); }
  body { position: relative; font-family: "Lato", sans-serif; color: var(--text); }

  .site-header {
    position: absolute; left: 0; top: 0; width: 1200px; height: 78px;
    background: var(--white);
    border-bottom: 3px solid #555;
    box-shadow: 0 2px 4px rgba(0,0,0,0.35);
  }
  .brand {
    position: absolute; left: 241px; top: 20px;
    font-family: "PT Sans Narrow", sans-serif; font-size: 40px; line-height: 1;
    color: var(--blue); letter-spacing: 1px;
  }
  .main-nav { position: absolute; top: 26px; left: 591px; display: flex; gap: 24px; }
  .main-nav a {
    font-family: "PT Sans Narrow", sans-serif; font-size: 22px; color: var(--ink);
    text-decoration: none; text-transform: uppercase; line-height: 1;
  }
  .main-nav a.active { color: var(--blue); }

  .hero-title {
    position: absolute; left: 0; width: 1200px; top: 122px; text-align: center;
    font-family: "PT Sans Narrow", sans-serif; font-weight: 400; font-size: 52px;
    color: var(--ink); text-transform: uppercase; line-height: 1;
  }
  .tagline {
    position: absolute; left: 0; width: 1200px; top: 196px; text-align: center;
    font-family: "PT Sans Narrow", sans-serif; font-size: 21px; color: var(--rust);
    text-transform: uppercase; line-height: 1;
  }

  .intro {
    position: absolute; left: 241px; top: 263px; width: 270px;
    font-size: 17.5px; line-height: 21.6px; color: var(--text);
  }
  .intro-photo {
    position: absolute; left: 526px; top: 267px; width: 435px; height: 295px;
    background: radial-gradient(ellipse at 55% 60%, #6b5636 0%, #3a2c1a 40%, #050403 80%);
  }

  .section-title {
    position: absolute; left: 0; width: 1200px; top: 614px; text-align: center;
    font-family: "PT Sans Narrow", sans-serif; font-weight: 400; font-size: 36px;
    color: var(--blue); text-transform: uppercase; line-height: 1;
  }

  .attorney {
    position: absolute; top: 688px; width: 220px; height: 220px; border-radius: 50%;
    overflow: hidden; border: 3px solid var(--white);
    box-shadow: 0 0 0 1px #cfcfcf, 0 2px 6px rgba(0,0,0,0.3);
  }
  .attorney--ostrand { left: 322px; }
  .attorney--marwick { left: 658px; }
  .attorney-photo { position: absolute; inset: 0; }
  .attorney--ostrand .attorney-photo { background: linear-gradient(180deg, #7d7466 0%, #4c4a4a 50%, #1d2130 100%); }
  .attorney--marwick .attorney-photo { background: linear-gradient(180deg, #cfcfcf 0%, #9a9a9a 50%, #5e5e5e 100%); }
  .attorney-name {
    position: absolute; left: 0; right: 0; top: 152px; height: 68px;
    padding-top: 8px; text-align: center;
    font-family: "PT Sans Narrow", sans-serif; font-size: 27px; color: var(--white); line-height: 1.1;
  }
  .attorney--ostrand .attorney-name { background: rgba(74,138,203,0.88); }
  .attorney--marwick .attorney-name { background: rgba(130,130,130,0.75); }

  .pointer { position: absolute; top: 918px; }
  .pointer--ostrand { left: 419px; }
  .pointer--marwick { left: 755px; }

  .bio-panel {
    position: absolute; left: 267px; top: 940px; width: 667px; height: 220px;
    background: var(--panel-blue); border-radius: 4px;
    padding: 17px 18px 0 19px;
    font-family: "PT Sans Narrow", sans-serif; font-size: 16.5px; line-height: 20px; color: var(--white);
  }
  .bio-panel p + p { margin-top: 19px; }
</style>
</head>
<body>
  <header class="site-header">
    <div class="brand">MOLAW</div>
    <nav class="main-nav">
      <a href="#" class="active">Home</a>
      <a href="#">About Us</a>
      <a href="#">Practice Areas</a>
      <a href="#">Contact Us</a>
    </nav>
  </header>

  <h1 class="hero-title">Marwick &amp; Ostrand Law</h1>
  <p class="tagline">Strong reputations don't go unnoticed.</p>

  <p class="intro">After practicing in both the private and public sector for several years, Rena Marwick and Theo Ostrand joined their legal expertise and formed Marwick &amp; Ostrand Law in 2015.&nbsp; With a combined 15 years of experience, Rena and Theo specialize in Civil Litigation, Family Law, Immigration and Criminal Defense. Their goal is to provide their clients with the best possible outcome in each and every case.</p>
  <div class="intro-photo" role="img" aria-label="Still life of antique leather books, an open volume and a globe on a wooden desk"></div>

  <h2 class="section-title">Who We Are</h2>

  <div class="attorney attorney--ostrand">
    <div class="attorney-photo" role="img" aria-label="Portrait of attorney Theo S. Ostrand in a dark suit"></div>
    <div class="attorney-name">Theo S. Ostrand</div>
  </div>
  <div class="attorney attorney--marwick">
    <div class="attorney-photo" role="img" aria-label="Black and white portrait of attorney Rena T. Marwick"></div>
    <div class="attorney-name">Rena T. Marwick</div>
  </div>

  <svg class="pointer pointer--ostrand" width="26" height="22" viewBox="0 0 26 22"><polygon points="13,0 26,22 0,22" fill="#5b94cf"/></svg>
  <svg class="pointer pointer--marwick" width="26" height="22" viewBox="0 0 26 22"><polygon points="13,0 26,22 0,22" fill="#808080"/></svg>

  <section class="bio-panel">
    <p>Theo Ostrand is a founding partner of Marwick &amp; Ostrand Law. After years of helping clients at other local civil litigation law firms, he started this firm so he could serve his clients with the care and devotion they deserve.</p>
    <p>When you are facing a legal issue, it is vital to select a skilled attorney who can understand your situation, and help you secure the most favorable resolution for you. Theo understands the law and is committed to providing the personal attention each client deserves.</p>
    <p>Theo's practice focuses on general civil litigation, family and immigration law. He has several years of experience helping clients in matters ranging from corporate disputes, fraud, breach of contract, intellectual property theft to employment disputes.</p>
  </section>
</body>
</html>
```